Gulf Book About Father - need cover design named - النور

The book talks about the good father who teaches his sons high principles and values, to be successful people in their lives.

Book size - 15 cm high
21 cm width
Data on the cover:
Name of the Book: النور
Author: دكتور/ مازن بن خليل القرطوني- Just write the name without the word writer
1440-2018
Logo of the Publishing House

Target Market(s)

Book submitted to children - Families - Schools - Public libraries

Requirements
Must have
• Design must include one or all of these options:
• The first option: a picture that has a meaning for a father who has values and principles with the son or children, expresses the contradiction - education, etc. -
• The background is to express the tender love or taken from the Emirates flag
• The second option: abstract art - with a background taken from the colors of the flag of the Emirates - or colors about love and tenderness
Should not have
• direct image

```html
<!DOCTYPE html>
<html lang="ar">
<head>
<meta charset="utf-8">
<title>النور – Book Cover</title>
<link rel="stylesheet" href="https://fonts.googleapis.com/css2?family=Lalezar&family=Open+Sans:wght@400&family=Noto+Sans+Arabic:wght@700&display=swap">
<style>
  :root {
    --flag-green: #2a8a22;
    --flag-red: #e31b37;
    --flag-black: #111111;
    --paper: #ffffff;
    --ink: #1a1a1a;
    --publisher-brown: #6b4328;
  }
  html, body {
    margin: 0;
    padding: 0;
    width: 800px;
    height: 1200px;
    overflow: hidden;
    background: var(--paper);
  }
  .cover {
    position: relative;
    width: 800px;
    height: 1200px;
    overflow: hidden;
    background: var(--paper);
    font-family: "Open Sans", sans-serif;
  }
  .pattern-band {
    position: absolute;
    left: 0;
    width: 800px;
  }
  .pattern-band--top {
    top: 0;
    height: 370px;
    background:
      linear-gradient(to bottom, rgba(255,255,255,0) 75%, var(--paper) 100%),
      linear-gradient(100deg, var(--flag-green) 0%, var(--flag-red) 35%, var(--flag-black) 55%, var(--flag-green) 75%, var(--flag-red) 100%);
    opacity: 0.9;
  }
  .pattern-band--bottom {
    bottom: 0;
    height: 380px;
    background:
      linear-gradient(to top, rgba(255,255,255,0) 80%, var(--paper) 100%),
      linear-gradient(80deg, var(--flag-green) 0%, var(--flag-black) 30%, var(--flag-red) 55%, var(--flag-green) 80%, var(--flag-black) 100%);
    opacity: 0.9;
  }
  .title {
    position: absolute;
    top: 395px;
    left: 0;
    width: 800px;
    height: 190px;
    margin: 0;
    text-align: center;
    font-family: "Lalezar", "Noto Sans Arabic", sans-serif;
    font-weight: 400;
    font-size: 200px;
    line-height: 190px;
    direction: rtl;
  }
  .title__outline,
  .title__fill {
    position: absolute;
    left: 0;
    top: 0;
    width: 800px;
  }
  .title__outline {
    color: var(--paper);
    -webkit-text-stroke: 16px var(--paper);
    filter: drop-shadow(0 0 2px rgba(0,0,0,0.35)) drop-shadow(0 3px 6px rgba(0,0,0,0.25));
  }
  .title__fill span {
    display: inline-block;
    background: linear-gradient(to right,
      var(--flag-green) 0%, var(--flag-green) 33.3%,
      var(--flag-red) 33.3%, var(--flag-red) 66.6%,
      var(--flag-black) 66.6%, var(--flag-black) 100%);
    -webkit-background-clip: text;
    background-clip: text;
    color: transparent;
  }
  .author {
    position: absolute;
    top: 594px;
    left: 0;
    width: 800px;
    margin: 0;
    text-align: center;
    font-size: 27px;
    font-weight: 400;
    color: var(--ink);
  }
  .publisher {
    position: absolute;
    top: 745px;
    left: 0;
    width: 800px;
    display: flex;
    justify-content: center;
    align-items: center;
    gap: 12px;
    direction: rtl;
  }
  .publisher__mark {
    width: 22px;
    height: 22px;
    background: var(--publisher-brown);
  }
  .publisher__name {
    font-family: "Noto Sans Arabic", sans-serif;
    font-weight: 700;
    font-size: 26px;
    color: var(--publisher-brown);
  }
</style>
</head>
<body>
  <main class="cover">
    <div class="pattern-band pattern-band--top" role="img" aria-label="Geometric triangle pattern in green, red, black and white"></div>

    <h1 class="title">
      <span class="title__outline" aria-hidden="true">النور</span>
      <span class="title__fill"><span>النور</span></span>
    </h1>
    <p class="author">Dr. Mazen bin Khalil Al - Qartouni</p>

    <div class="publisher">
      <span class="publisher__mark"></span>
      <span class="publisher__name">دار النخلة</span>
    </div>

    <div class="pattern-band pattern-band--bottom" role="img" aria-label="Geometric triangle pattern in green, red, black and white"></div>
  </main>
</body>
</html>
```